Rack Card Design Project

We are a locally family owned public golf course. We would like to have a rack card designed that can be used for multiple applications. The colors in our logo are grey, blue, and white. Please use those in the card design. The company logo, contact information, address, and summer pricing should be included. I've included some pictures that may or may not be used. I'm also open to suggestions....use one photo, multiple photos, a stock photo or image representing golf etc.

```html
<!DOCTYPE html>
<html lang="en">
<head>
<meta charset="UTF-8">
<title>Harbor Pines Golf Club – Summer Rates Rack Card</title>
<link href="https://fonts.googleapis.com/css2?family=Lato:wght@400;700;900&family=Luckiest+Guy&display=swap" rel="stylesheet">
<style>
  :root {
    --backdrop: #dcdce0;
    --paper: #efefe9;
    --navy: #12305a;
    --navy-box: #132f57;
    --ink: #111111;
    --grey: #8a8e93;
    --sky: #8fc4e6;
    --haze: #e9efe6;
    --fairway: #8fc04a;
    --grass: #5fa52a;
    --grass-dark: #3f8a1c;
    --red: #e0231c;
    --yellow: #f4e60c;
    --white: #ffffff;
  }
  html, body {
    margin: 0;
    width: 1200px;
    height: 1200px;
    overflow: hidden;
    background: var(--backdrop);
    font-family: 'Lato', sans-serif;
  }
  .rack-card {
    position: absolute;
    left: 340px;
    top: 35px;
    width: 520px;
    height: 1130px;
    background: var(--paper);
    overflow: hidden;
    box-shadow: 0 2px 10px rgba(0,0,0,0.15);
  }
  .hero-photo {
    position: absolute;
    left: 0; top: 0;
    width: 100%;
    height: 620px;
    background:
      linear-gradient(to bottom, rgba(239,239,233,0) 72%, var(--paper) 100%),
      linear-gradient(to bottom, var(--sky) 0%, var(--haze) 35%, var(--haze) 62%, var(--fairway) 74%, #b9d88a 88%, var(--paper) 100%);
  }
  .brand {
    position: absolute;
    left: 40px;
    top: 70px;
    display: flex;
    align-items: center;
    gap: 10px;
  }
  .brand-dot {
    width: 34px; height: 34px;
    border-radius: 50%;
    background: var(--navy);
  }
  .brand-name {
    font-weight: 900;
    font-size: 21px;
    line-height: 1.15;
    color: var(--navy);
    text-transform: uppercase;
  }
  .season-badge {
    position: absolute;
    left: 82px;
    top: 323px;
    width: 190px;
    height: 190px;
    border-radius: 50%;
    background: radial-gradient(circle at 40% 35%, #ffffff 0%, #eeeeee 55%, #cfcfcf 100%);
    display: flex;
    align-items: center;
    justify-content: center;
    text-align: center;
  }
  .season-title {
    font-family: 'Luckiest Guy', cursive;
    font-size: 33px;
    line-height: 1.15;
    color: var(--navy);
    letter-spacing: 1px;
    transform: skewX(-8deg);
    margin: 0;
  }
  .season-dates {
    position: absolute;
    left: 0; right: 0;
    top: 546px;
    margin: 0;
    text-align: center;
    font-family: 'Luckiest Guy', cursive;
    font-size: 36px;
    color: var(--white);
    -webkit-text-stroke: 1.6px var(--ink);
    letter-spacing: 0.5px;
  }
  .rate-col {
    position: absolute;
    top: 636px;
    text-align: center;
  }
  .rate-col--eighteen { left: 30px; width: 240px; }
  .rate-col--nine { left: 300px; width: 200px; }
  .rate-heading {
    font-weight: 900;
    font-size: 17px;
    color: var(--navy);
    margin: 0;
    letter-spacing: 0.2px;
  }
  .rate-list {
    list-style: none;
    margin: 30px 0 0;
    padding: 0;
    font-size: 21px;
    color: var(--ink);
    line-height: 32px;
  }
  .rate-list b { font-weight: 900; }
  .rate-price {
    font-weight: 900;
    font-size: 21px;
    color: var(--ink);
    margin: 4px 0 28px;
  }
  .column-divider {
    position: absolute;
    left: 282px;
    top: 675px;
    height: 80px;
    border-left: 2px dotted var(--ink);
  }
  .info-panel {
    position: absolute;
    left: 30px; right: 30px;
    top: 802px;
    height: 150px;
    background: var(--navy-box);
    border-radius: 12px;
    color: var(--white);
    padding: 0 16px;
    box-sizing: border-box;
  }
  .info-kids {
    margin: 30px 0 0;
    font-size: 20px;
  }
  .info-kids .free {
    font-family: 'Luckiest Guy', cursive;
    color: var(--red);
    font-size: 21px;
  }
  .info-lunch {
    margin: 26px 0 0;
    font-weight: 900;
    font-size: 20px;
  }
  .info-lunch .hours { color: var(--yellow); margin-left: 8px; }
  .grass-band {
    position: absolute;
    left: 0; right: 0; bottom: 0;
    height: 95px;
    background: linear-gradient(to bottom, rgba(95,165,42,0) 0%, var(--grass) 40%, var(--grass-dark) 100%);
  }
  .contact-call {
    position: absolute;
    left: 0; right: 0;
    top: 980px;
    margin: 0;
    text-align: center;
    font-weight: 900;
    font-size: 40px;
    color: var(--ink);
    letter-spacing: -0.5px;
  }
  .contact-web {
    position: absolute;
    left: 0; right: 0;
    top: 1040px;
    margin: 0;
    text-align: center;
    font-size: 27px;
    color: var(--ink);
  }
</style>
</head>
<body>
  <main class="rack-card">
    <div class="hero-photo" role="img" aria-label="Photo of a golfer mid-swing on a sunlit fairway with palm trees and ocean behind"></div>

    <div class="brand">
      <span class="brand-dot"></span>
      <span class="brand-name">Harbor Pines<br>Golf Club</span>
    </div>

    <div class="season-badge" role="img" aria-label="Golf ball">
      <h1 class="season-title">Summer<br>Rates</h1>
    </div>

    <p class="season-dates">MAY 1 - SEPTEMBER 30</p>

    <section class="rate-col rate-col--eighteen">
      <h2 class="rate-heading">18 HOLES WITH CART</h2>
      <ul class="rate-list">
        <li>7AM -11 AM &nbsp;<b>$24</b></li>
        <li>11 AM-3PM &nbsp;&nbsp;<b>$19</b></li>
        <li>3PM - CLOSE <b>$15</b></li>
      </ul>
    </section>

    <div class="column-divider"></div>

    <section class="rate-col rate-col--nine">
      <h2 class="rate-heading">9 HOLES WITH CART</h2>
      <p class="rate-price">$15</p>
      <h2 class="rate-heading">WALKING</h2>
      <p class="rate-price">$12</p>
    </section>

    <section class="info-panel">
      <p class="info-kids">Children 15 and Under <span class="free">FREE</span> with Paid Adult</p>
      <p class="info-lunch">LUNCH AVAILABLE DAILY:<span class="hours">10 AM - 3PM</span></p>
    </section>

    <div class="grass-band" role="img" aria-label="Photo of green grass along the bottom edge"></div>

    <p class="contact-call">CALL US: 555-014-2087</p>
    <p class="contact-web">www.harborpinesgolf.com</p>
  </main>
</body>
</html>
```